WBP Business Cards

I need business cards for "willow bend partners llc" doublesided... logo on the back (also include logo on front)
logo attached to project... i have jpg up.. let me know if you need eps file.
Company Info:
742 East Harlow Avenue, Suite 8D
Chicago, Illinois 60417
facsimile 312-481-2267 (list fax, address, website on all cards.)
www.willowbendpartnersllc.example
Three different people on cards:
Darius K. Whitcomb, CPA MST
Principal
ofc 312-481-3900
mobile 312-574-8816
dariuskwhitcomb@willowbendpartnersllc.example
Peter J. Olundsen, CPA MST
Principal
peterjolundsen@willowbendpartnersllc.example
mobile 708-613-4471
ofc 312-481-3900
Alvin M Crandby
Principal
ofc 312-481-3900
no mobile
alvinmcrandby@willowbendpartnersllc.example
I have multiple projects listed.. see below:
Business cards for willow bend partners llc
letterhead
envelopes
Business cards for KT Holdings LLC
letterhead
envelopes
Target Market(s)
rich people
Industry/Entity Type
Business
Look and feel

```html
<!DOCTYPE html>
<html lang="en">
<head>
<meta charset="utf-8">
<title>Willow Bend Partners LLC – Business Card</title>
<link rel="stylesheet" href="https://fonts.googleapis.com/css2?family=Fira+Sans:wght@400;500&display=swap">
<style>
  :root {
    --blue-deep: #0f2fc4;
    --blue-mid: #1448e0;
    --blue-bright: #0d6bf5;
    --brand-navy: #1a2f9e;
    --paper: #ffffff;
    --facet: rgba(255,255,255,0.05);
    --facet-dark: rgba(0,20,120,0.18);
  }
  html, body {
    margin: 0;
    padding: 0;
    width: 1200px;
    height: 777px;
    overflow: hidden;
    background: var(--paper);
  }
  .card {
    position: relative;
    width: 1200px;
    height: 777px;
    overflow: hidden;
    font-family: "Fira Sans", Arial, sans-serif;
  }
  .card-background {
    position: absolute;
    inset: 0;
  }
  .brand {
    position: absolute;
    left: 17px;
    top: 378px;
    width: 370px;
    text-align: center;
    color: var(--brand-navy);
  }
  .brand-mark {
    display: block;
    width: 70px;
    height: 70px;
    margin: 0 auto 34px;
    border-radius: 50%;
    background: var(--brand-navy);
  }
  .brand-name {
    font-size: 23px;
    font-weight: 500;
    letter-spacing: 1.2px;
    text-transform: uppercase;
    white-space: nowrap;
  }
  .company-details {
    position: absolute;
    left: 48px;
    top: 647px;
    margin: 0;
    font-style: normal;
    font-size: 17.5px;
    line-height: 24px;
    color: var(--brand-navy);
  }
  .person {
    position: absolute;
    left: 526px;
    top: 328px;
    padding-left: 24px;
    border-left: 2px solid var(--paper);
    color: var(--paper);
    font-size: 28px;
    line-height: 36px;
  }
  .person p { margin: 0; white-space: nowrap; }
  .person .email { font-size: 26.5px; }
</style>
</head>
<body>
<div class="card">
  <svg class="card-background" width="1200" height="777" viewBox="0 0 1200 777" aria-hidden="true">
    <defs>
      <linearGradient id="blueField" x1="0" y1="0" x2="1" y2="1">
        <stop offset="0" stop-color="var(--blue-deep)"/>
        <stop offset="0.5" stop-color="var(--blue-mid)"/>
        <stop offset="1" stop-color="var(--blue-bright)"/>
      </linearGradient>
      <radialGradient id="glow" cx="0.62" cy="0.55" r="0.5">
        <stop offset="0" stop-color="#3a78ff" stop-opacity="0.45"/>
        <stop offset="1" stop-color="#3a78ff" stop-opacity="0"/>
      </radialGradient>
    </defs>
    <rect width="1200" height="777" fill="url(#blueField)"/>
    <rect width="1200" height="777" fill="url(#glow)"/>
    <rect x="0" y="0" width="1200" height="115" fill="var(--facet-dark)"/>
    <polygon points="866,0 1200,0 1200,600 900,777 870,777" fill="var(--facet)"/>
    <polygon points="1090,777 1200,600 1200,777" fill="rgba(255,255,255,0.08)"/>
    <path d="M0,0 L197,0 C260,150 330,300 370,478 C395,590 410,690 418,777 L0,777 Z" fill="var(--paper)"/>
  </svg>

  <div class="brand">
    <span class="brand-mark"></span>
    <div class="brand-name">Willow Bend Partners llc</div>
  </div>

  <address class="company-details">
    742 East Harlow Avenue, Suite 8D<br>
    Chicago, Illinois 60417<br>
    facsimile 312-481-2267<br>
    www.willowbendpartnersllc.example
  </address>

  <div class="person">
    <p class="name">Peter J. Olundsen, CPA MST</p>
    <p class="title">Principal</p>
    <p class="email">peterjolundsen@willowbendpartnersllc.example</p>
    <p class="phone">mobile 708-613-4471</p>
    <p class="phone">ofc 312-481-3900</p>
  </div>
</div>
</body>
</html>
```